Design a business card for Brenton's Heat Guardian
Brenton's Heat Guardian
Design a business card for Brenton's Heat Guardian - Food
Creative Brief
Traditional
Hal Brenton
President and CEO
52894 Corvane Lane Clinton Township, MI 48052
hbrenton1947@mailvex.example
www.brentonsheatguardian.example
Simple color marks, with some white space to write notes

```html
<!DOCTYPE html>
<html lang="en">
<head>
<meta charset="utf-8">
<title>Brenton's Heat Guardian – Business Card</title>
<link rel="stylesheet" href="https://fonts.googleapis.com/css2?family=Open+Sans:wght@400;600;700&display=swap">
<style>
  :root {
    --backdrop: #8f9092;
    --card: #ffffff;
    --ink: #1f1f1f;
    --muted: #555555;
    --accent: #f07d1a;
    --rule: #d9d9d9;
    --faint: #ececec;
  }
  * { box-sizing: border-box; margin: 0; padding: 0; }
  html, body { width: 1200px; height: 908px; overflow: hidden; }
  body {
    background: var(--backdrop);
    font-family: "Open Sans", Arial, sans-serif;
    color: var(--ink);
    position: relative;
  }
  .card {
    position: absolute;
    width: 525px;
    height: 300px;
    background: var(--card);
    border-radius: 18px;
    box-shadow: 0 10px 30px rgba(0,0,0,0.25);
    overflow: hidden;
  }
  .card--front { left: 52px; top: 304px; }
  .card--back { left: 623px; top: 304px; }

  .front-decor {
    position: absolute; right: 40px; top: 30px;
    width: 190px; height: 150px; border-radius: 50%;
    background: radial-gradient(ellipse at center, var(--faint) 0%, rgba(236,236,236,0.4) 55%, rgba(255,255,255,0) 75%);
  }

  .wordmark { position: absolute; left: 40px; bottom: 48px; }
  .wordmark__name { font-weight: 700; font-size: 30px; line-height: 1.1; color: var(--ink); letter-spacing: -0.5px; }
  .wordmark__tag { font-weight: 600; font-size: 15px; color: var(--accent); margin-top: 2px; }

  .brand {
    position: absolute; left: 36px; top: 70px; width: 210px;
    display: flex; align-items: center; gap: 10px;
  }
  .brand__dot { width: 22px; height: 22px; border-radius: 50%; background: var(--accent); flex: none; }
  .brand__name { font-weight: 700; font-size: 21px; line-height: 1.15; color: var(--ink); }

  .divider { position: absolute; left: 262px; top: 40px; width: 1px; height: 220px; background: var(--rule); }

  .contact { position: absolute; left: 280px; top: 62px; width: 235px; list-style: none; font-size: 11.5px; color: var(--muted); }
  .contact li { display: flex; align-items: flex-start; gap: 8px; margin-bottom: 9px; line-height: 1.35; white-space: nowrap; }
  .contact svg { flex: none; margin-top: 1px; }

  .person { position: absolute; left: 40px; bottom: 46px; }
  .person__name { font-weight: 700; font-size: 19px; color: var(--ink); }
  .person__title { font-weight: 600; font-size: 13px; color: var(--accent); margin-top: 2px; }
</style>
</head>
<body>
  <section class="card card--front" aria-label="Card front">
    <div class="front-decor" role="img" aria-label="Faint cooking pot decoration"></div>
    <div class="wordmark">
      <div class="wordmark__name">Brenton's</div>
      <div class="wordmark__tag">Heat Guardian</div>
    </div>
  </section>

  <section class="card card--back" aria-label="Card back">
    <div class="brand">
      <span class="brand__dot"></span>
      <span class="brand__name">Brenton's Heat Guardian</span>
    </div>

    <div class="divider"></div>

    <ul class="contact">
      <li>
        <svg width="13" height="13" viewBox="0 0 14 14"><circle cx="7" cy="7" r="7" fill="#f07d1a"/><path d="M7 3.2a2.5 2.5 0 0 0-2.5 2.5C4.5 7.6 7 10.8 7 10.8s2.5-3.2 2.5-5.1A2.5 2.5 0 0 0 7 3.2z" fill="#fff"/></svg>
        <span>52894 Corvane Lane<br>Harlow Springs, OH 44890</span>
      </li>
      <li>
        <svg width="13" height="13" viewBox="0 0 14 14"><circle cx="7" cy="7" r="7" fill="#f07d1a"/><path d="M4.6 3.6l1.3 1.3-.7 1a5 5 0 0 0 2.9 2.9l1-.7 1.3 1.3-.9 1.1C6.9 10.3 3.7 7.1 3.5 4.5z" fill="#fff"/></svg>
        <span>555-014-2281</span>
      </li>
      <li>
        <svg width="13" height="13" viewBox="0 0 14 14"><circle cx="7" cy="7" r="7" fill="#f07d1a"/><path d="M4.6 3.6l1.3 1.3-.7 1a5 5 0 0 0 2.9 2.9l1-.7 1.3 1.3-.9 1.1C6.9 10.3 3.7 7.1 3.5 4.5z" fill="#fff"/></svg>
        <span>555-017-3390</span>
      </li>
      <li>
        <svg width="13" height="13" viewBox="0 0 14 14"><circle cx="7" cy="7" r="7" fill="#f07d1a"/><rect x="3.6" y="4.6" width="6.8" height="4.8" fill="none" stroke="#fff" stroke-width="1"/><path d="M3.6 4.6L7 7.3l3.4-2.7" fill="none" stroke="#fff" stroke-width="1"/></svg>
        <span>hbrenton1947@mailvex.example</span>
      </li>
      <li>
        <svg width="13" height="13" viewBox="0 0 14 14"><circle cx="7" cy="7" r="7" fill="#f07d1a"/><circle cx="7" cy="7" r="3.6" fill="none" stroke="#fff" stroke-width="0.9"/><path d="M3.4 7h7.2M7 3.4c-1.6 2-1.6 5.2 0 7.2M7 3.4c1.6 2 1.6 5.2 0 7.2" fill="none" stroke="#fff" stroke-width="0.8"/></svg>
        <span>www.brentonsheatguardian.example</span>
      </li>
    </ul>

    <div class="person">
      <div class="person__name">Hal Brenton</div>
      <div class="person__title">President and CEO</div>
    </div>
  </section>
</body>
</html>
```